Logo & Visitenkarte für Beratung im Bereich Seilbahnidustrie
very nice work. thank you very much! bk
Zielgruppe
Beratung im Bereich Seilbahnidustrie
Organisation eines internationalen (deutschsprachigen) Branchentreffs.
Aufgabenstellung
siehe PDF in der Anlage

```html
<!DOCTYPE html>
<html lang="de">
<head>
<meta charset="utf-8">
<title>Summit Meridian – Visitenkarte</title>
<link href="https://fonts.googleapis.com/css2?family=Encode+Sans+Condensed:wght@600&family=Encode+Sans+Expanded:wght@300;400&display=swap" rel="stylesheet">
<style>
  :root {
    --backdrop: #e6e6e6;
    --paper: #f7f7f5;
    --ink: #2b2b2b;
    --slate: #484848;
    --charcoal: #333333;
    --green: #2fae1a;
    --green-deep: #0f7a2a;
    --green-light: #5cc21c;
    --white: #ffffff;
  }
  * { margin: 0; padding: 0; box-sizing: border-box; }
  html, body {
    width: 1200px; height: 900px; overflow: hidden;
    background: var(--backdrop);
  }
  .sheet {
    position: relative; width: 1200px; height: 900px;
    display: flex; flex-direction: column; align-items: center;
    justify-content: center; gap: 33px;
  }
  .card {
    position: relative; width: 700px; height: 400px;
    overflow: hidden;
    box-shadow: 0 6px 18px rgba(0,0,0,0.12);
  }
  .card--front { background: var(--paper); }
  .card--back { background: var(--charcoal); }

  .brand-field {
    position: absolute; left: 0; top: 0; width: 290px; height: 400px;
  }
  .card--front .brand-field {
    background: linear-gradient(160deg, rgba(92,194,28,0.10) 0%, rgba(47,174,26,0.28) 60%, rgba(15,122,42,0.45) 100%);
  }
  .card--back .brand-field {
    left: auto; right: 0; width: 330px;
    background: linear-gradient(160deg, rgba(92,194,28,0.10) 0%, rgba(47,174,26,0.35) 100%);
  }

  .wordmark {
    position: absolute;
    display: flex; align-items: center; gap: 12px;
    font-family: "Encode Sans Condensed", "Arial Narrow", sans-serif;
    font-weight: 600; line-height: 0.95; letter-spacing: -0.5px;
  }
  .wordmark__name { display: block; }
  .wordmark__dot {
    flex: none; border-radius: 50%; border: 5px solid var(--green);
  }

  .card--front .wordmark {
    right: 18px; top: 84px; font-size: 40px; color: var(--slate);
    text-align: right;
  }
  .card--front .wordmark__dot { width: 62px; height: 62px; }

  .card--back .wordmark {
    left: 40px; top: 44px; font-size: 30px; color: var(--white);
  }
  .card--back .wordmark__dot { width: 44px; height: 44px; border-width: 4px; }

  .holder {
    position: absolute; right: 18px; top: 250px; text-align: right;
    font-family: "Encode Sans Expanded", Arial, sans-serif; color: var(--ink);
  }
  .holder__name { font-size: 21px; font-weight: 300; letter-spacing: 3.5px; }
  .holder__role { margin-top: 8px; font-size: 12px; letter-spacing: 2.5px; }

  .contact {
    position: absolute; right: 18px; top: 326px; text-align: right;
    list-style: none;
    font-family: "Encode Sans Expanded", Arial, sans-serif;
    font-size: 11.5px; font-weight: 300; letter-spacing: 1.6px;
    line-height: 18.5px; color: var(--ink);
  }
  .contact__domain { color: var(--green); }
</style>
</head>
<body>
<main class="sheet">
  <section class="card card--front" aria-label="Visitenkarte Vorderseite">
    <div class="brand-field" role="img" aria-label="Fläche für das grosse grüne Markenzeichen"></div>
    <div class="wordmark">
      <span>
        <span class="wordmark__name">SUMMIT</span>
        <span class="wordmark__name">MERIDIAN</span>
      </span>
      <span class="wordmark__dot" aria-hidden="true"></span>
    </div>
    <div class="holder">
      <p class="holder__name">JONAS BERGER</p>
      <p class="holder__role">C.E.O</p>
    </div>
    <ul class="contact">
      <li>043 555 0142</li>
      <li>berger@<span class="contact__domain">summitmeridian</span>.com</li>
      <li>www.<span class="contact__domain">summitmeridian</span>.com</li>
    </ul>
  </section>

  <section class="card card--back" aria-label="Visitenkarte Rückseite">
    <div class="brand-field" role="img" aria-label="Fläche für das grosse grüne Markenzeichen"></div>
    <div class="wordmark">
      <span class="wordmark__name">SUMMIT MERIDIAN</span>
      <span class="wordmark__dot" aria-hidden="true"></span>
    </div>
  </section>
</main>
</body>
</html>
```